Veltrano - Mechanic/Collision Center Business Card

We're looking for a business card design for our mechanic/ collision repair shop.

Can be with colours or monochromatic.

See the attached files.

Many thanks

```html
<!DOCTYPE html>
<html lang="pt">
<head>
<meta charset="utf-8">
<title>Veltrano – Business Card</title>
<link rel="stylesheet" href="https://fonts.googleapis.com/css2?family=Arimo:wght@400;700&display=swap">
<style>
  :root {
    --backdrop: #2b2b2d;
    --card: #0e0e0f;
    --card-edge: #1a1a1b;
    --accent: #1e9ad8;
    --text: #e9e9e9;
    --muted: #a9a9a9;
    --rule: #555;
  }
  * { box-sizing: border-box; margin: 0; padding: 0; }
  html, body {
    width: 1200px; height: 900px; overflow: hidden;
    background: var(--backdrop);
    font-family: "Arimo", Arial, sans-serif;
  }
  .stage { position: relative; width: 1200px; height: 900px; }
  .card {
    position: absolute; left: 337px;
    width: 525px; height: 300px;
    background: linear-gradient(160deg, var(--card-edge), var(--card) 60%);
    border-bottom: 9px solid var(--accent);
    box-shadow: 0 14px 30px rgba(0,0,0,.45);
  }
  .card--front { top: 110px; display: flex; align-items: center; justify-content: center; }
  .card--back  { top: 470px; text-align: center; padding-top: 36px; }

  .brand { display: flex; align-items: center; gap: 14px; }
  .brand__dot { width: 30px; height: 30px; border-radius: 50%; background: var(--accent); }
  .brand__name {
    font-weight: 700; font-size: 44px; letter-spacing: 2px;
    color: var(--text); text-transform: uppercase;
  }

  .person__name {
    color: var(--accent); font-size: 21px; letter-spacing: .5px;
    text-transform: uppercase;
  }
  .person__phone { color: var(--muted); font-size: 15px; margin-top: 3px; }

  .rule { width: 170px; height: 1px; background: var(--rule); margin: 8px auto; }
  .icons { display: flex; justify-content: center; gap: 5px; margin-bottom: 8px; }
  .icon {
    width: 22px; height: 22px; border-radius: 3px;
    background: var(--accent);
    display: flex; align-items: center; justify-content: center;
  }
  .contacts { color: var(--text); font-size: 15px; line-height: 19px; }

  .company__name {
    color: var(--accent); font-weight: 700; font-size: 15px;
    text-transform: uppercase; letter-spacing: .5px;
  }
  .company__address { color: var(--muted); font-size: 15px; line-height: 19px; }
</style>
</head>
<body>
<main class="stage">
  <section class="card card--front" aria-label="Card front">
    <div class="brand">
      <span class="brand__dot"></span>
      <span class="brand__name">Veltrano</span>
    </div>
  </section>

  <section class="card card--back" aria-label="Card back">
    <p class="person__name">Dário Valmonte</p>
    <p class="person__phone">+351 912 400 518</p>

    <div class="rule"></div>

    <div class="icons">
      <span class="icon" aria-label="Phone">
        <svg width="14" height="14" viewBox="0 0 24 24"><path fill="#0e0e0f" d="M6.6 10.8a15 15 0 0 0 6.6 6.6l2.2-2.2c.3-.3.7-.4 1-.2 1.1.4 2.3.6 3.6.6.6 0 1 .4 1 1V20c0 .6-.4 1-1 1A17 17 0 0 1 3 4c0-.6.4-1 1-1h3.5c.6 0 1 .4 1 1 0 1.3.2 2.5.6 3.6.1.3 0 .7-.2 1z"/></svg>
      </span>
      <span class="icon" aria-label="Email">
        <svg width="14" height="14" viewBox="0 0 24 24"><rect x="2" y="5" width="20" height="14" rx="1" fill="#0e0e0f"/><path d="M3 6l9 7 9-7" stroke="#1e9ad8" stroke-width="2" fill="none"/></svg>
      </span>
      <span class="icon" aria-label="Social page"></span>
    </div>

    <div class="contacts">
      <p>+351 210 455 732</p>
      <p>oficina@veltrano.pt</p>
      <p>www.veltrano.pt/social</p>
    </div>

    <div class="rule"></div>

    <p class="company__name">Veltrano, LDA</p>
    <div class="company__address">
      <p>Rua das Oficinas, 42</p>
      <p>1900-118 Lisboa</p>
    </div>
  </section>
</main>
</body>
</html>
```